Letterhead Design Project and Envelopes

MORVEN'S CLEANING SERVICES
4187 HALVERN RD. SUITE 213B
GLEN BURNIE, MD 21748

Target Market(s)

CLEANING SERVICESwww.morvenscleanpro.example

Industry/Entity Type

House Cleaning

Colors
0355a3
fbee3d
33a6d7

```html
<!DOCTYPE html>
<html lang="en">
<head>
<meta charset="utf-8">
<title>Morven's Cleaning Services – Letterhead</title>
<link href="https://fonts.googleapis.com/css2?family=Open+Sans:wght@400;600;700&family=Tinos:wght@400;700&display=swap" rel="stylesheet">
<style>
  :root {
    --brand-navy: #0355a3;
    --brand-yellow: #fbee3d;
    --brand-sky: #33a6d7;
    --band-yellow: #e4d51f;
    --band-blue: #06a8e6;
    --paper: #fbfbfb;
    --ink: #111111;
    --backdrop: #6a6a6a;
    --watermark: rgba(0, 0, 0, 0.045);
  }
  * { margin: 0; padding: 0; box-sizing: border-box; }
  html, body {
    width: 1200px;
    height: 1200px;
    overflow: hidden;
    background: var(--backdrop);
  }
  .letterhead {
    position: absolute;
    left: 226px;
    top: 40px;
    width: 748px;
    height: 1120px;
    background: var(--paper);
    overflow: hidden;
    font-family: "Tinos", "Times New Roman", serif;
    color: var(--ink);
  }
  .brand-mark {
    position: absolute;
    left: 66px;
    top: 78px;
    display: flex;
    align-items: center;
    gap: 8px;
  }
  .brand-mark .dot {
    width: 22px;
    height: 22px;
    border-radius: 50%;
    background: var(--brand-sky);
  }
  .brand-mark .name {
    font-family: "Open Sans", Arial, sans-serif;
    font-weight: 700;
    font-size: 30px;
    color: var(--brand-navy);
  }
  .watermark-name {
    position: absolute;
    left: 215px;
    top: 680px;
    width: 500px;
    text-align: center;
    font-family: "Open Sans", Arial, sans-serif;
    font-weight: 700;
    font-size: 96px;
    line-height: 120px;
    color: var(--watermark);
    transform: rotate(-55deg);
    transform-origin: center;
    white-space: nowrap;
  }
  .letter-line {
    position: absolute;
    left: 66px;
    width: 614px;
    font-size: 14.6px;
    line-height: 18px;
  }
  .letter-line sup { font-size: 9px; line-height: 0; }
  .justified { text-align: justify; }
  .recipient { top: 330px; }
  .reference { top: 440px; font-weight: 700; }
  .salutation { top: 512px; }
  .para-promotion { top: 548px; }
  .para-salary { top: 620px; }
  .para-receipt { top: 692px; }
  .closing { top: 764px; }
  .footer-band {
    position: absolute;
    left: 0;
    top: 1030px;
    width: 748px;
    height: 90px;
  }
  .footer-contact {
    position: absolute;
    left: 57px;
    top: 1050px;
    font-family: "Open Sans", Arial, sans-serif;
    font-size: 13.5px;
    line-height: 19px;
    color: var(--ink);
  }
  .footer-contact .company { font-weight: 600; }
  .footer-mark {
    position: absolute;
    right: 34px;
    top: 1060px;
    display: flex;
    align-items: center;
    gap: 6px;
  }
  .footer-mark .dot {
    width: 16px;
    height: 16px;
    border-radius: 50%;
    background: var(--brand-navy);
  }
  .footer-mark .name {
    font-family: "Open Sans", Arial, sans-serif;
    font-weight: 700;
    font-size: 22px;
    color: #ffffff;
  }
</style>
</head>
<body>
  <main class="letterhead">
    <div class="brand-mark">
      <span class="dot"></span>
      <span class="name">Morven's</span>
    </div>

    <div class="watermark-name" aria-hidden="true">Morven's</div>

    <div class="letter-line recipient">
      Name of employee: Mr. xyz<br>
      Address of employee<br>
      address line 2
    </div>

    <div class="letter-line reference">Ref: Promotion as an Assistant secretary</div>

    <p class="letter-line salutation">Dear Mr. xyz,</p>
    <p class="letter-line justified para-promotion">I have the pleasure to inform you that you have been promoted as assistant secretary in the share department of the company. You are required to take charge of the new assignment on 15<sup>th</sup> May, 2012. Please accept my hearty congratulations on your promotion.</p>
    <p class="letter-line justified para-salary">Your salary scale in the promoted cadre will be Tk. 16,000 and from 15th may, your basic salary will be fixed at Tk. 12,000 in the said scale. You will be entitled to all other allowances as applicable to the staff-II of the company. Other services conditions remain unchanged.</p>
    <p class="letter-line para-receipt">Please acknowledge receipt of this letter.</p>
    <p class="letter-line closing">Yours sincerely,</p>

    <svg class="footer-band" viewBox="0 0 748 90" width="748" height="90" aria-hidden="true">
      <rect x="0" y="0" width="748" height="90" fill="var(--band-blue)"/>
      <polygon points="0,0 600,0 585,83 0,83" fill="var(--band-yellow)"/>
      <rect x="0" y="83" width="748" height="7" fill="var(--band-blue)"/>
    </svg>

    <div class="footer-contact">
      <div class="company">MORVEN'S CLEANING SERVICES</div>
      <div>4187 HALVERN RD. SUITE 213B GLEN BURNIE, MD 21748</div>
    </div>

    <div class="footer-mark">
      <span class="dot"></span>
      <span class="name">Morven's</span>
    </div>
  </main>
</body>
</html>
```